Brivolan - presentation for a remote DBA team offering data platform management

We need a website design for wordpress site called Brivolan.cz
We deliver remote database and data platform administration and development, oversee the database administrators, consult and train the personnel responsible for the database operations. The website should include several sections, home page with graphics elements supporting the name and service - remote dba work; blog section; service introduction and description, team introduction and description, download section for documents, presentations etc.

Target Market(s)

small and medium business companies requiring remote DBA service

Number of Pages Required

3 page

Font styles to use
Sans Serif

Colors

Designer to choose colors to be used in the design.

Requirements
Must have
• The website should have several sections to introduce the services, blog, team introduction, downloads

```html
<!DOCTYPE html>
<html lang="en">
<head>
<meta charset="utf-8">
<title>Brivolan – Data Platform Management</title>
<link rel="stylesheet" href="https://fonts.googleapis.com/css2?family=Nunito:wght@300;400;600;700&family=Montserrat:wght@600;700&family=Ubuntu:wght@400;500;700&display=swap">
<style>
:root{
  --stage:#1c1c1e;
  --blue:#1f7fe3;
  --ink:#2a3038;
  --grey-text:#6d7480;
  --pale-text:#a9aeb6;
  --section-grey:#eceff2;
  --card-bar:#9a9a9a;
  --tab-dark:#2e3640;
  --footer:#1f2124;
  --white:#ffffff;
}
*{box-sizing:border-box;margin:0;padding:0}
html,body{width:1182px;height:1200px;overflow:hidden;background:var(--stage)}
body{font-family:'Nunito',sans-serif;color:var(--ink)}
.board{position:absolute;left:0;top:0;width:1478px;height:1500px;transform:scale(.7997);transform-origin:0 0}
.frame{position:absolute;background:var(--white);overflow:hidden}
.frame > *,.hero > *,.tabs > span,.news-card > *{position:absolute}
.frame-desktop{left:16px;top:16px;width:870px;height:1484px}
.frame-full{left:910px;top:18px;width:556px;height:1482px}
.hero{left:0;top:0;width:100%}
.hero-photo{left:0;top:0;width:100%;height:100%;background:linear-gradient(180deg,#1d6fd0 0%,#207ee2 45%,#2a8aea 100%)}
.brand{color:var(--white);font-family:'Ubuntu',sans-serif;font-weight:500;letter-spacing:.3px;white-space:nowrap}
.brand small{display:block;font-weight:400;letter-spacing:.2px}
.nav{color:var(--white);font-family:'Montserrat',sans-serif;font-weight:600;white-space:nowrap}
.nav span{display:inline-block}
.nav .is-active{opacity:.6}
.demo-btn{border:1px solid var(--white);color:var(--white);font-family:'Montserrat',sans-serif;font-weight:600;text-align:center;white-space:nowrap}
.hero-title{left:0;width:100%;text-align:center;color:var(--white);font-family:'Ubuntu',sans-serif;font-weight:400;white-space:nowrap}
.hero-title b{font-weight:700}
.hero-copy{text-align:center;color:var(--white);font-weight:600}
.explore{border:1px solid var(--white);color:var(--white);font-family:'Montserrat',sans-serif;font-weight:700;text-align:center}
.drop{background:var(--white);border-radius:50%}
.chev{color:#b8bcc3;text-align:center;width:20px}
.section-grey{left:0;width:100%;background:var(--section-grey)}
.heading{left:0;width:100%;text-align:center;font-weight:300;color:#4a5058;white-space:nowrap}
.rule{height:1px;background:#d5d8dc}
.para{text-align:center;color:var(--grey-text)}
.feature{text-align:center}
.feature h3{font-weight:400;color:var(--ink)}
.feature p{color:var(--pale-text)}
.client{color:#555b63;white-space:nowrap}
.dots{white-space:nowrap}
.dots i{display:inline-block;border-radius:50%;background:var(--ink)}
.dots i.on{background:var(--blue)}
.arrow{border-radius:50%;background:var(--white);box-shadow:0 1px 4px rgba(0,0,0,.18);color:var(--blue);text-align:center}
.service{background:var(--white);border-bottom:4px solid var(--card-bar);text-align:center}
.service span{display:block;font-family:'Montserrat',sans-serif;font-weight:700;color:var(--ink)}
.ring{border:1.5px solid var(--blue);border-radius:50%}
.tabs{font-family:'Montserrat',sans-serif;font-weight:700;color:var(--ink);white-space:nowrap}
.tab-bar{background:var(--tab-dark)}
.tab-bar-on{background:var(--blue)}
.label{font-family:'Montserrat',sans-serif;font-weight:700;color:var(--blue)}
.case-title{font-weight:600;color:var(--ink)}
.case-copy{color:var(--grey-text)}
.photo-shore{background:linear-gradient(180deg,#8fb0c4 0%,#6d8b6a 28%,#a9b3ae 45%,#d8d2c4 70%,#cfc2a8 100%)}
.news-card{background:var(--white);box-shadow:0 1px 3px rgba(0,0,0,.08)}
.news-meta{color:var(--pale-text)}
.news-text{color:var(--grey-text)}
.newsletter{left:0;width:100%;background:linear-gradient(180deg,#2f85e0,#2a7ad4)}
.footer{left:0;width:100%;background:var(--footer)}
.foot-link{color:var(--white);font-family:'Montserrat',sans-serif;font-weight:600;white-space:nowrap}
.social{border-radius:50%;background:#2a8be8}
</style>
</head>
<body>
<main class="board">

<section class="frame frame-desktop" aria-label="Home page, desktop view">
  <header class="hero" style="height:305px">
    <div class="hero-photo" role="img" aria-label="Blue tinted photo of a server room corridor"></div>
    <div class="brand" style="left:164px;top:9px;font-size:19px">BRIVOLAN<small style="font-size:8.5px;margin-top:1px">COMPLETE DATA SOLUTION</small></div>
    <div class="demo-btn" style="left:618px;top:3px;width:87px;height:15px;font-size:7px;line-height:13px">REQUEST A DEMO</div>
    <nav class="nav" style="left:388px;top:25px;font-size:7.6px">
      <span class="is-active" style="margin-right:14px">PRODUCTS</span><span style="margin-right:14px">SOLUTIONS</span><span style="margin-right:14px">WHY BRIVOLAN</span><span style="margin-right:14px">RESOURCES</span><span>ABOUT BRIVOLAN</span>
    </nav>
    <h1 class="hero-title" style="top:114px;font-size:19.5px">DBA team offering <b>DATA PLATFORM MANAGEMENT</b></h1>
    <p class="hero-copy" style="left:220px;top:150px;width:430px;font-size:8.6px;line-height:14px">Lorem Ipsum is simply dummy text of the printing and typesetting industry. Lorem Ipsum has been the industry's standard dummy text ever since the 1500s Lorem Ipsum is simply dummy text Lorem Ipsum is simply dummy text of the printing and typesetting industry.</p>
    <div class="explore" style="left:401px;top:205px;width:69px;height:25px;font-size:8px;line-height:23px">EXPLORE</div>
  </header>
  <div class="drop" style="left:423px;top:292px;width:24px;height:24px"></div>
  <div class="chev" style="left:425px;top:293px;font-size:9px">&#8964;</div>

  <h2 class="heading" style="top:334px;font-size:24px">Why Choose Ours</h2>
  <div class="rule" style="left:375px;top:369px;width:120px"></div>
  <svg style="left:237px;top:390px" width="36" height="36" viewBox="0 0 36 36"><circle cx="20" cy="20" r="15" fill="#e6e8eb"/><circle cx="17" cy="16" r="12" fill="#fff" stroke="#1f7fe3" stroke-width="1.5"/><circle cx="17" cy="16" r="8.5" fill="none" stroke="#1f7fe3"/><path d="M12 15h10M12 18h10" stroke="#1f7fe3"/></svg>
  <svg style="left:410px;top:390px" width="36" height="36" viewBox="0 0 36 36"><circle cx="21" cy="21" r="14" fill="#e6e8eb"/><path d="M17 5l10 4v8c0 7-5 11-10 13-5-2-10-6-10-13V9z" fill="#fff" stroke="#1f7fe3" stroke-width="1.5"/><circle cx="17" cy="17" r="5" fill="none" stroke="#1f7fe3"/><path d="M14.5 17l2 2 3.5-4" fill="none" stroke="#1f7fe3"/></svg>
  <svg style="left:581px;top:390px" width="36" height="36" viewBox="0 0 36 36"><circle cx="11" cy="12" r="9" fill="#e6e8eb"/><circle cx="18" cy="13" r="6" fill="#fff" stroke="#1f7fe3" stroke-width="1.5"/><path d="M6 33c1-7 6-10 12-10s11 3 12 10z" fill="#fff" stroke="#1f7fe3" stroke-width="1.5"/></svg>
  <div class="feature" style="left:185px;top:437px;width:140px"><h3 style="font-size:9.5px">100% Uptime Guarantee</h3><p style="font-size:7.4px;line-height:13px;margin-top:4px">Even the all-powerful Pointing has no control about the blind texts it is an almost unorthographic.</p></div>
  <div class="feature" style="left:357px;top:437px;width:140px"><h3 style="font-size:9.5px">Safe and Secured</h3><p style="font-size:7.4px;line-height:13px;margin-top:4px">Even the all-powerful Pointing has no control about the blind texts it is an almost unorthographic.</p></div>
  <div class="feature" style="left:529px;top:437px;width:140px"><h3 style="font-size:9.5px">Our Dedicated Support</h3><p style="font-size:7.4px;line-height:13px;margin-top:4px">Even the all-powerful Pointing has no control about the blind texts it is an almost unorthographic.</p></div>
  <div class="chev" style="left:425px;top:516px;font-size:9px">&#8964;</div>

  <h2 class="heading" style="top:555px;font-size:24px">Some of Our Clients</h2>
  <div class="client" style="left:165px;top:620px;font-size:11px;font-weight:700;letter-spacing:.5px">NORVALE</div>
  <div class="client" style="left:322px;top:616px;font-size:16px;font-weight:300">helvaro</div>
  <div class="client" style="left:443px;top:611px;font-size:23px;font-weight:700">lumetra</div>
  <div class="client" style="left:607px;top:616px;font-size:15px;font-weight:600">Ostrand</div>
  <div class="arrow" style="left:360px;top:676px;width:20px;height:20px;font-size:15px;line-height:18px">&#8249;</div>
  <div class="dots" style="left:400px;top:684px;font-size:0"><i style="width:4px;height:4px;margin-right:9px"></i><i style="width:4px;height:4px;margin-right:9px"></i><i style="width:4px;height:4px;margin-right:9px"></i><i class="on" style="width:6px;height:6px;margin-right:8px"></i><i style="width:4px;height:4px;margin-right:9px"></i><i style="width:4px;height:4px"></i></div>
  <div class="arrow" style="left:490px;top:676px;width:20px;height:20px;font-size:15px;line-height:18px">&#8250;</div>
  <div class="chev" style="left:425px;top:719px;font-size:9px">&#8964;</div>

  <div class="section-grey" style="top:732px;height:343px"></div>
  <h2 class="heading" style="top:766px;font-size:24px">DBA team offering data platform management</h2>
  <p class="para" style="left:280px;top:814px;width:310px;font-size:8.4px;line-height:13.6px">Lorem Ipsum is simply dummy text of the printing and typesetting industry. Lorem Ipsum has been the industry's standard dummy text ever since the 1500s, when an unknown printer took a galley of type and scrambled it to make a type specimen book.</p>
  <div class="service" style="left:165px;top:889px;width:134px;height:138px"><span style="font-size:8px;line-height:10px;margin-top:104px">DATA MANAGEMENT<br>PLATFORM</span></div>
  <div class="service" style="left:300px;top:889px;width:134px;height:138px"><span style="font-size:8px;margin-top:104px">DATA EXCHANGE</span></div>
  <div class="service" style="left:436px;top:889px;width:134px;height:138px"><span style="font-size:8px;margin-top:104px">CROSS-DEVICE</span></div>
  <div class="service" style="left:571px;top:889px;width:134px;height:138px"><span style="font-size:8px;margin-top:104px">AUDIENCE OPTIMIZER</span></div>
  <svg style="left:202px;top:914px" width="60" height="60" viewBox="0 0 60 60"><circle cx="30" cy="30" r="29" fill="none" stroke="#1f7fe3" stroke-width="1.5"/><rect x="17" y="18" width="26" height="20" fill="none" stroke="#1f7fe3"/><path d="M17 23h26M20 27h8M20 31h8M31 33l4-5 3 3 3-4" fill="none" stroke="#1f7fe3"/><path d="M24 42h12" stroke="#1f7fe3"/></svg>
  <svg style="left:337px;top:914px" width="60" height="60" viewBox="0 0 60 60"><circle cx="30" cy="30" r="29" fill="none" stroke="#1f7fe3" stroke-width="1.5"/><rect x="17" y="17" width="26" height="24" fill="none" stroke="#1f7fe3"/><circle cx="30" cy="30" r="6" fill="none" stroke="#1f7fe3"/><circle cx="30" cy="30" r="2" fill="#1f7fe3"/><path d="M17 22h26" stroke="#1f7fe3"/></svg>
  <svg style="left:473px;top:914px" width="60" height="60" viewBox="0 0 60 60"><circle cx="30" cy="30" r="29" fill="none" stroke="#1f7fe3" stroke-width="1.5"/><rect x="16" y="18" width="28" height="19" fill="none" stroke="#1f7fe3"/><circle cx="30" cy="27" r="5" fill="none" stroke="#1f7fe3"/><path d="M26 42h8M30 37v5" stroke="#1f7fe3"/></svg>
  <svg style="left:608px;top:914px" width="60" height="60" viewBox="0 0 60 60"><circle cx="30" cy="30" r="29" fill="none" stroke="#1f7fe3" stroke-width="1.5"/><rect x="17" y="17" width="26" height="22" fill="none" stroke="#1f7fe3"/><circle cx="33" cy="31" r="6" fill="none" stroke="#1f7fe3"/><path d="M33 25v6h6M21 22h8M21 26h5" fill="none" stroke="#1f7fe3"/></svg>
  <div class="drop" style="left:423px;top:1064px;width:24px;height:24px;background:var(--section-grey)"></div>
  <div class="chev" style="left:425px;top:1067px;font-size:9px">&#8964;</div>

  <h2 class="heading" style="top:1110px;font-size:24px">We are Help in few domains</h2>
  <p class="para" style="left:280px;top:1158px;width:310px;font-size:8.4px;line-height:13.6px">Lorem Ipsum is simply dummy text of the printing and typesetting industry. Lorem Ipsum has been the industry's standard dummy text ever since the 1500s, when an unknown printer took a galley of type and scrambled it to make a type specimen book.</p>
  <div class="tabs" style="left:232px;top:1229px;width:406px;height:14px;font-size:10.5px">
    <span style="left:37px;color:var(--blue)">AGENCIES</span><span style="left:148px">DIGITAL COMPANY</span><span style="left:318px">IT HUB</span>
  </div>
  <div class="tab-bar" style="left:232px;top:1249px;width:406px;height:4px"></div>
  <div class="tab-bar-on" style="left:232px;top:1249px;width:135px;height:4px"></div>
  <svg style="left:294px;top:1252px" width="10" height="6" viewBox="0 0 10 6"><path d="M0 0h10L5 5z" fill="#1f7fe3"/></svg>

  <div class="label" style="left:232px;top:1296px;font-size:7px">CASE STUDY</div>
  <div class="case-title" style="left:232px;top:1308px;width:180px;font-size:15px;line-height:18px">Kestrel Agency Increases Engagement 250% with Cross-Device Targeting</div>
  <p class="case-copy" style="left:232px;top:1367px;width:178px;font-size:8px;line-height:11.8px">Lorem Ipsum is simply dummy text of the printing and typesetting industry. Lorem Ipsum has been the industry's standard dummy text ever since the 1500s.</p>
  <div class="case-copy" style="left:232px;top:1451px;font-size:8px;line-height:12px">-Jory<br>VP INTEGRATED MEDIA, ORVIK</div>
  <div class="photo-shore" role="img" aria-label="Photo of puppies running along a lake shore" style="left:415px;top:1319px;width:275px;height:170px"></div>
  <div class="arrow" style="left:163px;top:1338px;width:38px;height:38px;font-size:28px;line-height:34px">&#8249;</div>
  <div class="arrow" style="left:668px;top:1338px;width:38px;height:38px;font-size:28px;line-height:34px">&#8250;</div>
</section>

<section class="frame frame-full" aria-label="Home page, full length">
  <header class="hero" style="height:195px">
    <div class="hero-photo" role="img" aria-label="Blue tinted photo of a server room corridor"></div>
    <div class="brand" style="left:105px;top:6px;font-size:11.5px">BRIVOLAN<small style="font-size:5px">COMPLETE DATA SOLUTION</small></div>
    <div class="demo-btn" style="left:395px;top:2px;width:56px;height:9px;font-size:4.4px;line-height:8px">REQUEST A DEMO</div>
    <nav class="nav" style="left:248px;top:16px;font-size:4.6px">
      <span class="is-active" style="margin-right:9px">PRODUCTS</span><span style="margin-right:9px">SOLUTIONS</span><span style="margin-right:9px">WHY BRIVOLAN</span><span style="margin-right:9px">RESOURCES</span><span>ABOUT BRIVOLAN</span>
    </nav>
    <h1 class="hero-title" style="top:74px;font-size:11.8px">DBA team offering <b>DATA PLATFORM MANAGEMENT</b></h1>
    <p class="hero-copy" style="left:140px;top:96px;width:276px;font-size:5.3px;line-height:8.6px">Lorem Ipsum is simply dummy text of the printing and typesetting industry. Lorem Ipsum has been the industry's standard dummy text ever since the 1500s Lorem Ipsum is simply dummy text. Lorem Ipsum is simply dummy text of the printing and typesetting industry.</p>
    <div class="explore" style="left:256px;top:131px;width:44px;height:15px;font-size:5px;line-height:13px">EXPLORE</div>
  </header>
  <div class="drop" style="left:270px;top:187px;width:15px;height:15px"></div>

  <h2 class="heading" style="top:214px;font-size:14.5px">Why Choose Ours</h2>
  <svg style="left:153px;top:249px" width="22" height="22" viewBox="0 0 36 36"><circle cx="18" cy="18" r="13" fill="#fff" stroke="#1f7fe3" stroke-width="2"/><circle cx="18" cy="18" r="8" fill="none" stroke="#1f7fe3" stroke-width="1.5"/></svg>
  <svg style="left:262px;top:249px" width="22" height="22" viewBox="0 0 36 36"><path d="M18 4l10 4v8c0 7-5 11-10 13-5-2-10-6-10-13V8z" fill="#fff" stroke="#1f7fe3" stroke-width="2"/><circle cx="18" cy="17" r="5" fill="none" stroke="#1f7fe3" stroke-width="1.5"/></svg>
  <svg style="left:372px;top:249px" width="22" height="22" viewBox="0 0 36 36"><circle cx="18" cy="12" r="6" fill="#fff" stroke="#1f7fe3" stroke-width="2"/><path d="M6 32c1-7 6-10 12-10s11 3 12 10z" fill="#fff" stroke="#1f7fe3" stroke-width="2"/></svg>
  <div class="feature" style="left:118px;top:279px;width:92px"><h3 style="font-size:5.8px">100% Uptime Guarantee</h3><p style="font-size:4.5px;line-height:7.8px;margin-top:3px">Even the all-powerful Pointing has no control about the blind texts it is an almost unorthographic.</p></div>
  <div class="feature" style="left:227px;top:279px;width:92px"><h3 style="font-size:5.8px">Safe and Secured</h3><p style="font-size:4.5px;line-height:7.8px;margin-top:3px">Even the all-powerful Pointing has no control about the blind texts it is an almost unorthographic.</p></div>
  <div class="feature" style="left:337px;top:279px;width:92px"><h3 style="font-size:5.8px">Our Dedicated Support</h3><p style="font-size:4.5px;line-height:7.8px;margin-top:3px">Even the all-powerful Pointing has no control about the blind texts it is an almost unorthographic.</p></div>

  <h2 class="heading" style="top:355px;font-size:14.5px">Some of Our Clients</h2>
  <div class="client" style="left:105px;top:397px;font-size:7px;font-weight:700">NORVALE</div>
  <div class="client" style="left:205px;top:394px;font-size:10px;font-weight:300">helvaro</div>
  <div class="client" style="left:283px;top:391px;font-size:14px;font-weight:700">lumetra</div>
  <div class="client" style="left:388px;top:394px;font-size:9px;font-weight:600">Ostrand</div>
  <div style="left:233px;top:431px;color:var(--blue);font-size:10px">&#8249;</div>
  <div class="dots" style="left:256px;top:436px;font-size:0"><i style="width:2.5px;height:2.5px;margin-right:5px"></i><i style="width:2.5px;height:2.5px;margin-right:5px"></i><i style="width:2.5px;height:2.5px;margin-right:5px"></i><i class="on" style="width:4px;height:4px;margin-right:5px"></i><i style="width:2.5px;height:2.5px;margin-right:5px"></i><i style="width:2.5px;height:2.5px"></i></div>
  <div style="left:316px;top:431px;color:var(--blue);font-size:10px">&#8250;</div>

  <div class="section-grey" style="top:468px;height:220px"></div>
  <h2 class="heading" style="top:490px;font-size:14.5px">DBA team offering data platform management</h2>
  <p class="para" style="left:180px;top:521px;width:196px;font-size:4.9px;line-height:8.5px">Lorem Ipsum is simply dummy text of the printing and typesetting industry. Lorem Ipsum has been the industry's standard dummy text ever since the 1500s, when an unknown printer took a galley of type and scrambled it to make a type specimen book.</p>
  <div class="service" style="left:105px;top:568px;width:86px;height:89px;border-bottom-width:3px"><span style="font-size:5px;line-height:6px;margin-top:64px">DATA MANAGEMENT<br>PLATFORM</span></div>
  <div class="service" style="left:192px;top:568px;width:86px;height:89px;border-bottom-width:3px"><span style="font-size:5px;margin-top:64px">DATA EXCHANGE</span></div>
  <div class="service" style="left:279px;top:568px;width:86px;height:89px;border-bottom-width:3px"><span style="font-size:5px;margin-top:64px">CROSS-DEVICE</span></div>
  <div class="service" style="left:366px;top:568px;width:85px;height:89px;border-bottom-width:3px"><span style="font-size:5px;margin-top:64px">AUDIENCE OPTIMIZER</span></div>
  <div class="ring" style="left:129px;top:584px;width:38px;height:38px"></div>
  <div class="ring" style="left:216px;top:584px;width:38px;height:38px"></div>
  <div class="ring" style="left:303px;top:584px;width:38px;height:38px"></div>
  <div class="ring" style="left:389px;top:584px;width:38px;height:38px"></div>
  <svg style="left:137px;top:593px" width="214" height="20" viewBox="0 0 214 20"><rect x="3" y="3" width="16" height="13" fill="none" stroke="#1f7fe3"/><rect x="90" y="3" width="16" height="14" fill="none" stroke="#1f7fe3"/><circle cx="98" cy="10" r="3.5" fill="none" stroke="#1f7fe3"/><rect x="177" y="3" width="16" height="12" fill="none" stroke="#1f7fe3"/><circle cx="185" cy="9" r="3" fill="none" stroke="#1f7fe3"/></svg>
  <svg style="left:399px;top:593px" width="20" height="20" viewBox="0 0 20 20"><rect x="2" y="3" width="16" height="14" fill="none" stroke="#1f7fe3"/><circle cx="12" cy="11" r="3.5" fill="none" stroke="#1f7fe3"/></svg>

  <h2 class="heading" style="top:710px;font-size:14.5px">We are Help in few domains</h2>
  <p class="para" style="left:180px;top:741px;width:196px;font-size:4.9px;line-height:8.5px">Lorem Ipsum is simply dummy text of the printing and typesetting industry. Lorem Ipsum has been the industry's standard dummy text ever since the 1500s, when an unknown printer took a galley of type and scrambled it to make a type specimen book.</p>
  <div class="tabs" style="left:148px;top:786px;width:260px;height:9px;font-size:6.3px">
    <span style="left:24px;color:var(--blue)">AGENCIES</span><span style="left:95px">DIGITAL COMPANY</span><span style="left:203px">IT HUB</span>
  </div>
  <div class="tab-bar" style="left:148px;top:798px;width:260px;height:2.5px"></div>
  <div class="tab-bar-on" style="left:148px;top:798px;width:86px;height:2.5px"></div>

  <div class="label" style="left:148px;top:828px;font-size:4.2px">CASE STUDY</div>
  <div class="case-title" style="left:148px;top:836px;width:115px;font-size:9.2px;line-height:11.5px">Kestrel Agency Increases Engagement 250% with Cross-Device Targeting</div>
  <p class="case-copy" style="left:148px;top:874px;width:108px;font-size:4.7px;line-height:7.2px">Lorem Ipsum is simply dummy text of the printing and typesetting industry. Lorem Ipsum has been the industry's standard dummy text ever since the 1500s.</p>
  <div class="case-copy" style="left:148px;top:926px;font-size:4.7px;line-height:8px">-Jory<br>VP INTEGRATED MEDIA, ORVIK</div>
  <div class="case-copy" style="left:148px;top:949px;font-size:4.3px;text-decoration:underline;font-weight:700">VIEW ALL CASE STUDIES</div>
  <div class="photo-shore" role="img" aria-label="Photo of puppies running along a lake shore" style="left:265px;top:843px;width:176px;height:128px"></div>
  <div class="arrow" style="left:104px;top:857px;width:22px;height:22px;font-size:16px;line-height:20px">&#8249;</div>
  <div class="arrow" style="left:428px;top:857px;width:22px;height:22px;font-size:16px;line-height:20px">&#8250;</div>

  <div class="section-grey" style="top:982px;height:225px"></div>
  <h2 class="heading" style="top:1005px;font-size:14.5px">News &amp; Resources</h2>
  <p class="para" style="left:180px;top:1035px;width:196px;font-size:4.9px;line-height:8.5px">Lorem Ipsum is simply dummy text of the printing and typesetting industry. Lorem Ipsum has been the industry's standard dummy text ever</p>
  <div class="news-card" style="left:121px;top:1066px;width:101px;height:122px">
    <div role="img" aria-label="Photo of a desk with a laptop and notes" style="left:0;top:0;width:101px;height:62px;background:linear-gradient(135deg,#dfe3e6,#f4f4f2 60%,#c9cdd0)"></div>
    <div class="news-meta" style="left:7px;top:71px;font-size:3.8px">August 12, 2018 · Admin · 3</div>
    <div class="news-text" style="left:7px;top:84px;width:85px;font-size:5px;line-height:8.4px">Even the all-powerful Pointing has no control about the blind texts</div>
  </div>
  <div class="news-card" style="left:231px;top:1066px;width:101px;height:122px">
    <div role="img" aria-label="Photo of a person holding up a blue device" style="left:0;top:0;width:101px;height:62px;background:linear-gradient(180deg,#dfe4e8,#9bbbd6 55%,#cfd5da)"></div>
    <div class="news-meta" style="left:7px;top:71px;font-size:3.8px">August 12, 2018 · Admin · 3</div>
    <div class="news-text" style="left:7px;top:84px;width:85px;font-size:5px;line-height:8.4px">Even the all-powerful Pointing has no control about the blind texts</div>
  </div>
  <div class="news-card" style="left:341px;top:1066px;width:101px;height:122px">
    <div role="img" aria-label="Abstract pink and violet fluid texture" style="left:0;top:0;width:101px;height:62px;background:linear-gradient(135deg,#e4a9cf,#c7b4ea 45%,#f3c6d6 80%,#b9c8ee)"></div>
    <div class="news-meta" style="left:7px;top:71px;font-size:3.8px">August 12, 2018 · Admin · 3</div>
    <div class="news-text" style="left:7px;top:84px;width:85px;font-size:5px;line-height:8.4px">Even the all-powerful Pointing has no control about the blind texts</div>
  </div>

  <div class="newsletter" style="top:1207px;height:151px"></div>
  <h2 class="heading" style="top:1254px;font-size:11px;font-weight:400;color:var(--white)">Subcribe to our Newsletter</h2>
  <p class="para" style="left:180px;top:1273px;width:196px;font-size:4.3px;line-height:8px;color:#d7e8fb">Far far away, behind the word mountains, far from the countries Vokalia and Consonantia, there live the blind texts. Separated they live in.</p>
  <div style="left:233px;top:1304px;width:88px;height:14px;border:1px solid #8fbdf0;border-radius:7px"></div>
  <div style="left:240px;top:1307px;font-size:4.5px;color:#cfe3fa">Enter email address</div>
  <svg style="left:308px;top:1307px" width="8" height="8" viewBox="0 0 8 8"><path d="M1 4l6-3-2 6-1-2z" fill="#fff"/></svg>

  <footer class="footer" style="top:1358px;height:124px"></footer>
  <div class="brand" style="left:103px;top:1380px;font-size:8px">BRIVOLAN<small style="font-size:3.5px">COMPLETE DATA SOLUTION</small></div>
  <svg style="left:190px;top:1380px" width="6" height="30" viewBox="0 0 6 30"><path d="M3 0a2.5 2.5 0 012.5 2.5C5.5 4.5 3 7 3 7S.5 4.5.5 2.5A2.5 2.5 0 013 0z" fill="#2a8be8"/><rect x="0" y="16" width="6" height="4" fill="none" stroke="#2a8be8" stroke-width=".8"/></svg>
  <div style="left:201px;top:1381px;font-size:4px;color:#fff">See Our Locations</div>
  <div style="left:201px;top:1395px;font-size:4px;color:#fff">info@brivolan.cz</div>
  <div style="left:190px;top:1408px;font-size:3.8px;color:#6b7077">NEWSLETTER SIGNUP</div>
  <div style="left:190px;top:1420px;width:60px;height:9px;background:#fff"></div>
  <div style="left:193px;top:1422px;font-size:3.6px;color:#9aa0a7">Email Address</div>
  <div class="foot-link" style="left:190px;top:1434px;width:60px;height:9px;background:var(--blue);font-size:4px;line-height:9px;text-align:center">SUBMIT</div>
  <div class="foot-link" style="left:295px;top:1378px;font-size:4.3px"><span style="margin-right:14px">CONTACT US</span><span style="margin-right:14px">CAREERS</span><span style="margin-right:20px">EVENTS</span><span>AWARDS</span></div>
  <div class="foot-link" style="left:295px;top:1402px;width:55px;height:8px;background:var(--blue);font-size:3.8px;line-height:8px;text-align:center">REQUEST A DEMO</div>
  <div class="social" style="left:397px;top:1402px;width:9px;height:9px"></div>
  <div class="social" style="left:412px;top:1402px;width:9px;height:9px"></div>
  <div class="social" style="left:427px;top:1402px;width:9px;height:9px"></div>
  <div class="social" style="left:442px;top:1402px;width:9px;height:9px"></div>
  <div style="left:103px;top:1463px;font-size:3.6px;color:#7d8289;white-space:nowrap">Copyright ©2018 Brivolan Solutions, Inc. &nbsp;&nbsp; | &nbsp; Privacy Center &nbsp; | &nbsp; Opt Out &nbsp; | &nbsp; Site Map</div>
</section>

</main>
</body>
</html>
```